Modern Medical Optometry Website

We need mordern, Patient friendly website. Easy to navigate and enhance our advance medical technology and excellent patient care.
1. HOME PAGE
2. OUR TEAM PAGE
3. EYECARE PAGE - VISION SERVICES, EYE EXAMS, KERATOCONUS CENTER, GLAUCOMA , DIABITES, TORVANEX EXAM, DIGITAL RETINAL, OCT.
4. MYOPIA CONTROL CLINIC
5. DRY EYE CLINIC
6. EYEWEAR
7. PATIENT CENTER - BLOG
7. CONTACT US
This is our current website www.brindlecove.com
and We want to add more content and a cleaner design like these website
http://tamsworthoptometry.com/
https://www.klmhaven.com/

```html
<!DOCTYPE html>
<html lang="en">
<head>
<meta charset="utf-8">
<title>Brindle Cove Optometry</title>
<link href="https://fonts.googleapis.com/css2?family=Open+Sans:wght@400;500;600;700;800&display=swap" rel="stylesheet">
<style>
:root{
  --blue:#0a9ccb;
  --blue-dark:#0787b0;
  --yellow:#f6c81e;
  --ink:#333;
  --ink-soft:#555;
  --white:#fff;
  --line:#e4e4e4;
}
*{margin:0;padding:0;box-sizing:border-box}
html,body{width:811px;height:1200px;overflow:hidden;background:var(--white);font-family:"Open Sans",sans-serif;color:var(--ink)}
.page{position:relative;width:811px;height:1200px}
.hero{position:absolute;left:0;top:0;width:811px;height:444px;
  background:linear-gradient(180deg,#3e5f9e 0%,#5a6fae 35%,#7d6fa8 65%,#4b5c9c 100%)}
.hero-shade{position:absolute;inset:0;background:radial-gradient(ellipse at 50% 55%,rgba(214,170,160,.45),rgba(40,70,140,.2) 60%,rgba(30,55,120,.35))}
.brand{position:absolute;left:18px;top:14px;width:99px;height:98px;background:var(--white);border-radius:3px;display:flex;flex-direction:column;align-items:center;justify-content:center;gap:8px}
.brand-mark{width:34px;height:34px;background:var(--yellow)}
.brand-name{font-size:9px;font-weight:600;color:#777;text-align:center;line-height:1.2;letter-spacing:.5px}
.hours{position:absolute;left:241px;top:15px;display:flex;align-items:center;gap:7px}
.hours-label{font-size:6.5px;color:var(--white);line-height:1.4}
.hours-label b{display:block;color:var(--yellow);font-weight:700;font-size:7px}
.search{position:absolute;left:586px;top:18px;width:96px;height:14px;background:var(--blue);border-radius:2px;font-size:7px;color:var(--white);padding:2px 0 0 16px}
.search svg{position:absolute;right:4px;top:2px}
.social{position:absolute;left:723px;top:19px;display:flex;gap:6px}
.social span{width:10px;height:10px;background:var(--white);border-radius:2px;opacity:.9}
.nav{position:absolute;left:248px;top:73px;display:flex;gap:13.5px;font-size:9.3px;font-weight:700;color:var(--white);white-space:nowrap}
.nav .current{color:var(--yellow)}
.headline{position:absolute;left:0;width:811px;text-align:center;font-weight:800;color:var(--white);font-size:29px;letter-spacing:1px}
.headline.one{top:154px}
.headline.two{top:213px;color:var(--yellow)}
.btn{position:absolute;top:309px;height:24px;width:135px;display:flex;align-items:center;justify-content:center;font-size:9px;font-weight:700;color:var(--white);letter-spacing:.3px}
.btn.solid{left:228px;background:var(--blue)}
.btn.ghost{left:448px;border:1px solid var(--white)}
.locations{position:absolute;left:86px;top:411px;width:647px;height:111px;background:var(--white);border-top:3px solid var(--blue);box-shadow:0 2px 4px rgba(0,0,0,.2);display:flex}
.location{width:50%;padding:8px 0 0 24px;font-size:8.7px;line-height:15.2px;color:var(--ink)}
.location + .location{border-left:1px solid #f3e3b8;padding-left:45px}
.location h3{font-size:10.5px;font-weight:700;margin-bottom:5px}
.direct{color:var(--blue);margin-left:16px}
.loc-pin{position:absolute;left:303px;top:13px}
.corner{position:absolute;width:6px;height:6px;border-radius:50%;background:var(--blue)}
.features{position:absolute;left:0;top:562px;width:811px;display:flex;justify-content:space-between;padding:0 47px 0 49px}
.feature{width:240px;text-align:center}
.feature h2{font-size:14px;font-weight:500;margin:14px 0 8px;color:var(--ink)}
.feature p{font-size:11px;line-height:20.3px;color:var(--ink-soft)}
.feature a{display:block;margin-top:6px;font-size:11px;font-weight:600;color:var(--blue);text-decoration:none;letter-spacing:.3px}
.promise{position:absolute;left:0;top:804px;width:395px;height:358px;background:var(--blue);color:var(--white);box-shadow:0 2px 3px rgba(0,0,0,.25)}
.promise-title{position:absolute;left:0;top:42px;width:413px;text-align:center}
.promise-title h2{display:inline-block;font-size:15px;font-weight:700;letter-spacing:.5px;padding:0 3px 4px;border-bottom:1px solid rgba(255,255,255,.7)}
.promise p{position:absolute;left:19px;width:372px;font-size:10.4px;line-height:16.9px}
.promise .p1{top:106px}
.promise .p2{top:207px}
.promise-photo{position:absolute;left:397px;top:804px;width:407px;height:358px;background:linear-gradient(135deg,#f1f2f3 0%,#e6dfd8 45%,#d9a47a 62%,#c9d2dc 100%)}
</style>
</head>
<body>
<div class="page">
  <header class="hero">
    <div class="hero-shade" role="img" aria-label="Photo of a smiling child wearing an optometrist's trial frame during an eye exam"></div>
    <div class="brand"><span class="brand-mark"></span><span class="brand-name">BRINDLE COVE<br>OPTOMETRY</span></div>
    <div class="hours">
      <svg width="17" height="17" viewBox="0 0 20 20"><circle cx="10" cy="10" r="9" fill="#fff"/><path d="M10 4v6l4 2" stroke="#3e5f9e" stroke-width="2" fill="none"/></svg>
      <div class="hours-label">WORKING HOURS<b>TODAY : 9AM - 6PM</b></div>
    </div>
    <div class="search">Search<svg width="10" height="10" viewBox="0 0 10 10"><circle cx="4" cy="4" r="3" stroke="#fff" stroke-width="1.4" fill="none"/><path d="M6.3 6.3l3 3" stroke="#fff" stroke-width="1.4"/></svg></div>
    <div class="social"><span></span><span></span><span></span><span></span></div>
    <nav class="nav">
      <span class="current">HOME</span><span>OUR TEAM</span><span>EYECARE ⌄</span><span>MYOPIA CONTROL CLINIC</span><span>DRY EYE CLINIC</span><span>EYEWEAR</span><span>BLOG</span><span>CONTACT</span>
    </nav>
    <h1 class="headline one">HELPING YOU ACHIEVE AND MAINTAIN</h1>
    <div class="headline two">HEALTHY EYESIGHT</div>
    <div class="btn solid">MAKE AN APPOINTMENT</div>
    <div class="btn ghost">CONTACT US</div>
  </header>

  <section class="locations">
    <div class="location">
      <h3>Brindle Cove Optometry</h3>
      4820 Larkfield Ave.<br>Alderwood, CA 91402<br>Phone. 555-014-2210<br>Fax. 555-014-2270<br>
      Email. info@brindlecove.com <span class="direct">Get Directions ▸</span>
    </div>
    <div class="location">
      <h3>Fernridge</h3>
      9183 Halvern St.,<br>Suite 4,<br>Fernridge, CA 91418<br>Phone. 555-019-4020<br>
      Email. fernridge@brindlecove.com <span class="direct">Get Directions ▸</span>
    </div>
    <svg class="loc-pin" width="34" height="48" viewBox="0 0 34 48"><path d="M17 0C7.6 0 0 7.6 0 17c0 12 17 31 17 31s17-19 17-31C34 7.6 26.4 0 17 0z" fill="#eee"/><circle cx="17" cy="16" r="6" fill="#fff"/></svg>
    <span class="corner" style="left:5px;bottom:8px"></span>
    <span class="corner" style="right:5px;bottom:3px"></span>
  </section>

  <section class="features">
    <div class="feature">
      <svg width="34" height="34" viewBox="0 0 34 34"><circle cx="17" cy="17" r="14.5" stroke="#0a9ccb" stroke-width="3" fill="none"/><path d="M17 9v9l6 4" stroke="#0a9ccb" stroke-width="3" fill="none"/></svg>
      <h2>Opening Hours</h2>
      <p>Monday - Thursday: 9 am - 6 pm<br>Friday: 8.30 am - 5 pm<br>Saturday: 8.30 am- 5 pm<br>Closed on Sundays</p>
      <a>LEARN MORE</a>
    </div>
    <div class="feature">
      <svg width="40" height="34" viewBox="0 0 40 34"><rect x="1.5" y="1.5" width="37" height="31" rx="2" stroke="#0a9ccb" stroke-width="3" fill="none"/><rect x="1.5" y="9" width="37" height="5" fill="#0a9ccb"/><rect x="6" y="20" width="7" height="4" fill="#0a9ccb"/><rect x="15" y="20" width="11" height="4" fill="#0a9ccb"/></svg>
      <h2>FlexPay Health</h2>
      <p>We proudly accept FlexPay Health<br>cards at our practice. The program<br>allows you make low monthly pay-<br>ments for healthcare procedures.</p>
      <a>LEARN MORE</a>
    </div>
    <div class="feature">
      <svg width="46" height="34" viewBox="0 0 46 34"><circle cx="14" cy="8" r="7" fill="#0a9ccb"/><path d="M0 32c0-10 6-14 14-14s14 4 14 14z" fill="#0a9ccb"/><circle cx="34" cy="12" r="6" fill="#0a9ccb"/><path d="M24 32c0-8 5-12 11-12s11 4 11 12z" fill="#0a9ccb"/></svg>
      <h2>ClearPlan Premier</h2>
      <p>We are proud to announce we<br>are a ClearPlan Premier Office! Get the<br>most out of your membership<br>at our office.</p>
      <a>LEARN MORE</a>
    </div>
  </section>

  <section class="promise">
    <div class="promise-title"><h2>THE BRINDLE COVE PROMISE</h2></div>
    <p class="p1">Welcome to Brindle Cove Optometry, where your vision and eye health are our sole priority. We take great pride in providing you with state-of-the-art eyecare matched with personal attention from our staff and doctors. Your quality of life is our goal and we believe that healthy eyesight is vital to achieving it.</p>
    <p class="p2">Our professional and personable staff is highly trained in helping you achieve and maintain healthy eyesight. Our optometrists have combined experiences and specialize in Orthokeratology (OrthoK), Ocular disease, Glaucoma diagnosis &amp; management.</p>
    <span class="corner" style="right:5px;top:5px;background:var(--yellow)"></span>
    <span class="corner" style="right:3px;bottom:5px;background:var(--yellow)"></span>
  </section>
  <div class="promise-photo" role="img" aria-label="Photo of a mother and daughter in an optometry exam room with eye testing equipment"></div>
</div>
</body>
</html>
```